Geschäftspapiere für Rechtsanwaltskanzlei
Zielgruppe
Rechtsanwaltskanzlei als Einzelkanzlei, Schwerpunkt: Immobilienrecht
Aufgabenstellung
Das Design soll modern abstrakt sein und Stärke und Kompromisslosigkeit assoziieren ( wie das bereits vorhandene Logo). Die Informationen im vorhandenen Briefbogen müssen alle übernommen werden.
Wir benötigen 4 Betreffzeilen: Unser Zeichen, Ihr Zeichen, wer ./.wen und kurze Beschreibung des Falles.
Das schwarze Logo soll übernommen werden, gerne hätten wir noch eine zweite Farbe ( rot oder blau ) im Briefbogen in Form von Balken oder Hervorhebung von Text.

```html
<!DOCTYPE html>
<html lang="de">
<head>
<meta charset="utf-8">
<title>Kelvar Rechtsanwaltskanzlei – Briefbogen</title>
<link href="https://fonts.googleapis.com/css2?family=Open+Sans:wght@400;600;700&display=swap" rel="stylesheet">
<style>
  :root {
    --backdrop: #dcdbde;
    --paper: #ffffff;
    --ink: #111111;
    --accent: #3a7cc9;
    --faint: #f3f3f3;
  }
  * { margin: 0; padding: 0; box-sizing: border-box; }
  html, body { width: 1200px; height: 1200px; overflow: hidden; }
  body { background: var(--backdrop); font-family: "Open Sans", Arial, sans-serif; color: var(--ink); }
  .letterhead {
    position: absolute; left: 302px; top: 179px; width: 595px; height: 842px;
    background: var(--paper);
  }
  .brand { position: absolute; left: 68px; top: 29px; display: flex; align-items: flex-end; gap: 8px; }
  .brand-mark { width: 40px; height: 40px; background: var(--ink); }
  .brand-name { font-weight: 700; font-size: 13px; letter-spacing: .3px; line-height: 1; color: var(--ink); }
  .rule { position: absolute; left: 68px; width: 499px; height: 1px; background: var(--accent); }
  .rule--head { top: 116px; }
  .rule--foot-top { top: 722px; }
  .rule--foot-bottom { top: 813px; }
  .sender { position: absolute; left: 68px; top: 141px; font-size: 5.6px; line-height: 8px; }
  .sender .firm { color: var(--accent); font-weight: 700; }
  .reference { position: absolute; left: 354px; top: 140px; list-style: none;
    color: var(--accent); font-weight: 600; font-size: 7.6px; line-height: 12px; }
  .reference .gap { height: 12px; }
  .fold-mark { position: absolute; left: 0; width: 20px; height: 1px; }
  .fold-mark--upper { top: 297px; background: var(--accent); }
  .fold-mark--punch { top: 420px; background: var(--ink); }
  .backdrop-name { position: absolute; left: 186px; top: 358px; width: 223px; height: 126px;
    display: flex; align-items: center; justify-content: center;
    font-weight: 700; font-size: 46px; color: var(--faint); letter-spacing: 2px; }
  .footer { position: absolute; top: 736px; left: 0; width: 100%; font-size: 6.8px; line-height: 9px; }
  .footer-col { position: absolute; top: 0; }
  .footer-col h4 { color: var(--accent); font-weight: 600; font-size: 6.8px; }
  .footer-col strong { font-weight: 700; }
  .footer-col .spacer { height: 9px; }
  .col-firm { left: 68px; }
  .col-muelheim { left: 189px; }
  .col-dellbrueck { left: 322px; }
  .col-bank { left: 455px; }
  .kv { display: grid; grid-template-columns: 28px auto; }
  .kv.bank { grid-template-columns: 21px auto; }
</style>
</head>
<body>
  <main class="letterhead">
    <header class="brand">
      <span class="brand-mark"></span>
      <span class="brand-name">KELVAR RECHTSANWALTSKANZLEI</span>
    </header>
    <div class="rule rule--head"></div>

    <p class="sender"><span class="firm">Kelvar Rechtsanwaltskanzlei</span> | Marlene Vossberg-Adami<br>Lindenhofer Weg 212b | 51069 Köln (Dellbrück)</p>

    <ul class="reference">
      <li>Ihr Zeichen:</li>
      <li>Ihre Nachricht vom:</li>
      <li>Unser Zeichen:</li>
      <li>Unsere Nachricht vom:</li>
      <li>Beschreibung des Falles:</li>
      <li class="gap"></li>
      <li>Name:</li>
      <li>Telefon:</li>
      <li>Telefax:</li>
      <li>E-Mail:</li>
      <li class="gap"></li>
      <li>Datum:</li>
    </ul>

    <span class="fold-mark fold-mark--upper"></span>
    <span class="fold-mark fold-mark--punch"></span>

    <div class="backdrop-name" aria-hidden="true">KELVAR</div>

    <div class="rule rule--foot-top"></div>
    <footer class="footer">
      <div class="footer-col col-firm">
        <h4>Kelvar Anwaltskanzlei</h4>
        <div class="spacer"></div>
        <strong>Rechtsanwältin<br>Marlene Vossberg-Adami</strong><br>
        Fachanwältin für Mietrecht<br>und WEG-Recht
      </div>
      <div class="footer-col col-muelheim">
        <h4>Büro Köln-Mülheim</h4>
        Ahornstraße 18<br>51063 Köln
        <div class="kv"><span>Telefon:</span><span>+49 (0) 221 555 018 42</span>
        <span>Telefax:</span><span>+49 (0) 221 555 073 90</span>
        <span>Mobil:</span><span>+49 (0) 1570 555 20 64</span>
        <span>E-Mail:</span><span>info@kelvarkanzlei.de</span></div>
      </div>
      <div class="footer-col col-dellbrueck">
        <h4>Büro Köln Dellbrück</h4>
        Lindenhofer Weg 212b<br>51069 Köln
        <div class="kv"><span>Telefon:</span><span>+49 (0) 221 5550917</span>
        <span>Telefax:</span><span>+49 (0) 221 555 073 90</span>
        <span>Mobil:</span><span>+49 (0) 1570 555 20 64</span>
        <span>E-Mail:</span><span>info@kelvarkanzlei.de</span></div>
      </div>
      <div class="footer-col col-bank">
        <h4>Bankverbindung:</h4>
        Stadtsparkasse Rheinufer
        <div class="kv bank"><span>IBAN:</span><span>DE00123450000000000000</span>
        <span>BIC:</span><span>RHNUDE00XXX</span></div>
      </div>
    </footer>
    <div class="rule rule--foot-bottom"></div>
  </main>
</body>
</html>
```